Unternehmensvorstellung : Broschüre DIN A4 ca. 6 Innenseiten.
Zielgruppe
Dienstleistungen:
- Messdienst und Erstellung Heiz- und Nebenkostenabrechung für Mieter
- Rauchwarnmelder Montage und Wartung
- Trinkwasser/Legionellenprüfung
- Energie-Monitoring-Service (automatisch Ermittlung günstigster Versorger)
Für:
Immobilienverwalter
Immobilienbesitzer
Immobilien Gesellschaften
Architekten und Planer
Aufgabenstellung
siehe Homepage www.dorelkatum.de

```html
<!DOCTYPE html>
<html lang="de">
<head>
<meta charset="utf-8">
<title>Dorelkatum – Broschüre Umschlag</title>
<link rel="stylesheet" href="https://fonts.googleapis.com/css2?family=Barlow:wght@400;500;700&family=Fira+Sans+Condensed:wght@700&display=swap">
<style>
  :root {
    --brand-blue: #0a86c8;
    --brand-red: #e2412b;
    --paper: #ffffff;
    --photo-light: #eef0f1;
    --photo-mid: #d9dde0;
    --photo-navy: #2b3552;
  }
  html, body { margin: 0; padding: 0; overflow: hidden; }
  body { width: 1200px; height: 424px; background: var(--paper); }
  .spread { position: relative; width: 1200px; height: 424px; overflow: hidden; font-family: "Barlow", sans-serif; }

  /* Back cover */
  .back-cover { position: absolute; left: 0; top: 0; width: 600px; height: 424px; background: var(--brand-blue); }
  .back-cover__band { position: absolute; left: 0; top: 28px; width: 600px; height: 100px; background: var(--paper); }
  .back-cover__url { position: absolute; left: 31px; top: 97px; margin: 0; font-weight: 700; font-size: 13px; color: var(--brand-red); letter-spacing: 0.2px; }
  .back-cover__contact { position: absolute; left: 31px; top: 300px; color: var(--paper); font-size: 7px; line-height: 8.6px; letter-spacing: 0.3px; }
  .back-cover__contact p { margin: 0 0 8px; }
  .back-cover__imprint { position: absolute; left: 30px; top: 381px; color: var(--paper); font-size: 5.4px; line-height: 7.2px; letter-spacing: 0.2px; margin: 0; }

  /* Front cover */
  .front-cover { position: absolute; left: 600px; top: 0; width: 600px; height: 424px; }
  .front-cover__art { position: absolute; inset: 0; }
  .front-cover__quote { position: absolute; left: 335px; top: 43px; width: 240px; margin: 0; text-align: center;
    font-family: "Fira Sans Condensed", sans-serif; font-weight: 700; font-size: 15.5px; line-height: 20.5px; color: var(--paper); letter-spacing: 0.2px; }
  .front-cover__brand { position: absolute; right: 34px; top: 352px; margin: 0; font-family: "Barlow", sans-serif;
    font-weight: 700; font-size: 27px; color: var(--brand-blue); letter-spacing: 0.5px; display: flex; align-items: center; gap: 6px; }
  .front-cover__brand-mark { width: 20px; height: 20px; background: var(--brand-blue); }
</style>
</head>
<body>
<div class="spread">
  <section class="back-cover">
    <div class="back-cover__band"></div>
    <p class="back-cover__url">dorelkatum.de</p>
    <div class="back-cover__contact">
      <p>Dorelkatum Deutschland GmbH</p>
      <p>Lindenweg 14<br>63110 Bergheim</p>
      <p>+49 (0) 6021 - 48 302 17<br>kontor@dorelkatum.de</p>
    </div>
    <p class="back-cover__imprint">Printed in Germany | Edition 01/2017<br>© Copyright Dorelkatum</p>
  </section>

  <section class="front-cover">
    <svg class="front-cover__art" width="600" height="424" viewBox="0 0 600 424">
      <defs>
        <linearGradient id="photoTone" x1="0" y1="0" x2="1" y2="1">
          <stop offset="0" stop-color="var(--photo-light)"/>
          <stop offset="0.55" stop-color="var(--photo-mid)"/>
          <stop offset="1" stop-color="#c9cdd2"/>
        </linearGradient>
        <radialGradient id="photoFigure" cx="0.5" cy="0.8" r="0.5">
          <stop offset="0" stop-color="var(--photo-navy)" stop-opacity="0.55"/>
          <stop offset="1" stop-color="var(--photo-navy)" stop-opacity="0"/>
        </radialGradient>
      </defs>
      <g role="img" aria-label="Foto: Servicetechniker im Arbeitsanzug mit Klemmbrett vor einer Heizungsanlage">
        <polygon points="0,0 600,0 600,288 0,359" fill="url(#photoTone)"/>
        <polygon points="0,0 600,0 600,288 0,359" fill="url(#photoFigure)"/>
      </g>
      <polygon class="front-cover__stripe" points="0,359 600,288 600,324 0,374" fill="var(--brand-blue)"/>
      <polygon class="front-cover__bubble" points="332,40 578,30 567,118 497,118 461,153 461,118 351,116" fill="var(--brand-blue)"/>
    </svg>
    <p class="front-cover__quote">„WIR BIETEN MEHR ALS<br>NUR DEN KLASSISCHEN<br>MESSDIENST.“</p>
    <p class="front-cover__brand">DORELKATUM<span class="front-cover__brand-mark"></span></p>
  </section>
</div>
</body>
</html>
```